依頼概要
■ 依頼の目的/概要

弊社は「カード選びナビ広場」というクレジットカードの比較サイトを運営しています。
サイトリニューアルにあたり、「人気・おすすめカテゴリを厳選」部分のデザインをお願いします。コーディングは不要です。

「人気・おすすめカテゴリを厳選」はトップページとカテゴリ別ページで表示しています。
トップページ: http://www.sorairo-cardnavi.example/
カテゴリ別ページ: http://www.sorairo-cardnavi.example/search/category/id/10/

具体的には添付ファイルの赤枠で囲んである部分です。

```html
<!DOCTYPE html>
<html lang="ja">
<head>
<meta charset="utf-8">
<title>カード選びナビ広場</title>
<link rel="stylesheet" href="https://fonts.googleapis.com/css2?family=Noto+Sans+JP:wght@400;700&display=swap">
<style>
:root{
  --blue:#1f6fc3;
  --blue-dark:#124f96;
  --blue-pale:#e3eefa;
  --line:#c9d7e6;
  --orange:#f08a1c;
  --orange-pale:#fff1dc;
  --yellow-pale:#fff8df;
  --text:#333;
  --muted:#777;
  --red:#d9342b;
  --bg:#fff;
}
*{box-sizing:border-box;margin:0;padding:0}
html,body{width:1200px;height:2968px;overflow:hidden}
body{font-family:"Noto Sans JP",sans-serif;color:var(--text);background:var(--bg);font-size:14px;line-height:1.6;position:relative}
a{color:var(--blue);text-decoration:none}
.site-header{height:48px;display:flex;align-items:center;justify-content:space-between;padding:0 20px}
.brand{display:flex;align-items:center;gap:10px;font-weight:700;font-size:24px;color:var(--blue)}
.brand-mark{width:18px;height:18px;background:var(--orange);border-radius:50%}
.tagline{font-size:13px;color:var(--muted)}
.global-nav{height:32px;background:var(--blue);display:flex;padding:0 20px;gap:4px}
.global-nav a{color:#fff;font-size:13px;font-weight:700;padding:0 22px;line-height:32px;border-right:1px solid rgba(255,255,255,.35)}
.global-nav a.current{background:var(--blue-dark)}
.page{display:flex;gap:24px;padding:14px 20px 0}
.main{width:868px}
.side{width:268px}
.intro{font-size:13px;height:60px}
.section{border:1px solid var(--line);margin-bottom:14px}
.section-title{background:linear-gradient(var(--blue),var(--blue-dark));color:#fff;font-weight:700;font-size:14px;padding:6px 12px;display:flex;justify-content:space-between}
.section-title small{font-weight:400;font-size:11px;opacity:.85}
.featured-cards{display:grid;grid-template-columns:repeat(4,1fr);gap:14px;padding:14px}
.card-item{text-align:center;font-size:12px}
.card-item h3{font-size:13px;color:var(--blue);margin-bottom:6px}
.card-visual{height:110px;border-radius:8px;background:linear-gradient(135deg,#6fa7df,#1f4f8c)}
.card-item p{text-align:left;margin:8px 0;height:72px}
.btn{display:block;background:linear-gradient(#f7a84b,var(--orange));color:#fff;font-weight:700;border-radius:4px;padding:8px 0;text-align:center;font-size:13px}
.category-box{margin:14px;background:var(--yellow-pale);border:2px solid var(--orange);border-radius:8px;padding:12px 16px;display:flex;gap:20px}
.category-box h3{font-size:16px;color:var(--orange);margin-bottom:8px}
.category-list{list-style:none;display:grid;grid-template-columns:1fr 1fr;gap:6px 30px;width:560px}
.category-list li{background:#fff;border:1px solid #f2c98e;border-radius:4px;padding:5px 10px;font-size:13px;font-weight:700;display:flex;align-items:center;gap:8px}
.category-list li::before{content:"";width:14px;height:14px;border-radius:50%;background:var(--orange)}
.category-side{flex:1;display:flex;flex-direction:column;gap:10px;padding-top:36px}
.brand-badge{height:44px;background:var(--blue-pale);border:1px solid var(--line);border-radius:4px}
.link-block{padding:10px 14px}
.link-block h4{font-size:13px;margin-bottom:8px}
.link-grid{list-style:none;display:grid;grid-template-columns:repeat(3,1fr);gap:6px 20px;font-size:12px}
.link-grid li::before{content:"› ";color:var(--blue)}
.more{font-size:11px;text-align:right;padding:8px 14px}
.pick-head{font-size:13px;font-weight:700;padding:10px 14px;color:var(--blue)}
.pick-grid{display:grid;grid-template-columns:1fr 1fr;gap:16px 30px;padding:0 14px 14px}
.pick{display:flex;gap:12px;font-size:12px}
.pick-photo{width:200px;height:120px;background:linear-gradient(#8ec9ee,#3c8fce 60%,#e8dcb8)}
.pick p{width:170px}
.life{padding:16px}
.life-cards{display:grid;grid-template-columns:1fr 1fr;gap:20px}
.life-card{border:1px solid var(--line);border-radius:6px;padding:12px;font-size:12px}
.life-card h3{display:flex;align-items:center;gap:10px;font-size:14px;color:var(--blue);margin-bottom:10px}
.q{width:36px;height:36px;border-radius:50%;background:var(--blue);color:#fff;display:flex;align-items:center;justify-content:center;font-size:18px}
.q.alt{background:var(--red)}
.life-card .card-visual{height:120px;width:200px;margin:0 auto 10px}
.life-banner{margin:20px auto 12px;width:620px;border:3px solid #9cc4ea;border-radius:30px;text-align:center;font-size:22px;font-weight:700;color:var(--blue);padding:8px}
.life-text{font-size:12px;text-align:center;line-height:1.9}
.life-text .hl{color:var(--red);font-weight:700}
.life-buttons{display:flex;justify-content:center;gap:40px;margin-top:16px}
.life-buttons .btn{width:240px;font-size:18px;padding:14px 0}
.life-buttons .btn.blue{background:linear-gradient(#5aa0e0,var(--blue))}
.side-banner{height:110px;background:linear-gradient(var(--blue-pale),#bcd8f3);border:1px solid var(--line);text-align:center;padding-top:22px;margin-bottom:12px}
.side-banner strong{display:block;color:var(--red);font-size:28px}
.side-box{border:1px solid var(--line);margin-bottom:12px}
.side-box .body{padding:10px;font-size:12px;display:flex;gap:8px}
.side-box .card-visual{width:100px;height:64px;flex:none}
.campaign{padding:10px;font-size:12px;border-bottom:1px dashed var(--line)}
.campaign h5{color:var(--blue);font-size:12px}
.campaign .tag{margin:6px 0;background:var(--orange);color:#fff;font-weight:700;text-align:center;border-radius:4px;padding:8px 0;font-size:15px}
.campaign .note{color:var(--red)}
.site-footer{position:absolute;left:0;top:2830px;width:1200px;height:138px;border-top:3px solid var(--blue);background:var(--blue-pale);padding:16px 20px;font-size:12px;display:flex;justify-content:space-between}
.search{display:flex;gap:6px;align-items:center}
.search span{width:260px;height:24px;background:#fff;border:1px solid var(--line)}
.search b{background:var(--blue);color:#fff;padding:2px 12px;border-radius:3px;font-weight:400}
</style>
</head>
<body>
<header class="site-header">
  <div class="brand"><span class="brand-mark"></span>カード選びナビ広場</div>
  <p class="tagline">カード選びナビ広場はクレジットカードの総合情報サイトです。</p>
</header>
<nav class="global-nav">
  <a class="current">ホーム</a><a>クレジットカードを探す</a><a>クレジットカード比較</a><a>クレジットカードランキング</a><a>お問い合わせ</a>
</nav>
<div class="page">
  <main class="main">
    <p class="intro">クレジットカードにはさまざまな特典があります。<br>よく使うお店や目的から、あなたのライフスタイルに合ったクレジットカードを選んでみましょう。</p>

    <section class="section">
      <h2 class="section-title">注目のクレジットカード<small>ピックアップ</small></h2>
      <div class="featured-cards">
        <div class="card-item"><h3>ソラ銀<br>クラシックカード</h3><div class="card-visual" role="img" aria-label="カード券面"></div><p>年会費初年度無料。海外旅行保険付きで初めての一枚に最適です。</p><a class="btn">詳しく見る</a></div>
        <div class="card-item"><h3>ミライ<br>ポイントカード</h3><div class="card-visual" role="img" aria-label="カード券面"></div><p>誕生月はポイント3倍。毎日の買い物でポイントが貯まります。</p><a class="btn">詳しく見る</a></div>
        <div class="card-item"><h3>ナギサ<br>ゴールドカード</h3><div class="card-visual" role="img" aria-label="カード券面"></div><p>空港ラウンジが無料。充実の補償で出張や旅行も安心です。</p><a class="btn">詳しく見る</a></div>
        <div class="card-item"><h3>ホシノ<br>カードプラス</h3><div class="card-visual" role="img" aria-label="カード券面"></div><p>ネット通販でポイント還元率アップ。即日発行にも対応。</p><a class="btn">詳しく見る</a></div>
      </div>
    </section>

    <section class="section">
      <h2 class="section-title">カテゴリからクレジットカードを探す<small>カテゴリ</small></h2>
      <div class="category-box">
        <div>
          <h3>人気・おすすめカテゴリを厳選</h3>
          <ul class="category-list">
            <li>ETCカード一体型</li><li>年会費永年無料</li>
            <li>海外旅行に強い</li><li>スタンダードカード</li>
            <li>ポイント還元率が高い</li><li>ショッピング保険付き</li>
            <li>ゴールドカード</li><li>入会キャンペーン実施中</li>
            <li>マイルが貯まる</li><li>即日発行できる</li>
            <li>学生におすすめ</li><li>国際ブランドで選ぶ</li>
          </ul>
        </div>
        <div class="category-side">
          <div class="brand-badge" role="img" aria-label="国際ブランドA"></div>
          <div class="brand-badge" role="img" aria-label="国際ブランドB"></div>
          <div class="brand-badge" role="img" aria-label="国際ブランドE"></div>
        </div>
      </div>
      <div class="link-block">
        <h4>その他のカテゴリ</h4>
        <ul class="link-grid">
          <li>家族カードが作れる</li><li>電子マネー対応</li><li>女性におすすめ</li>
          <li>ガソリン代がお得</li><li>ショッピング専用</li><li>法人・ビジネス向け</li>
          <li>リボ払い専用</li><li>旅行保険が自動付帯</li><li>提携カード</li>
        </ul>
      </div>
      <p class="more"><a>全てのカテゴリを見る（カテゴリ一覧へ）</a></p>
    </section>

    <section class="section">
      <h2 class="section-title">クレジットカード特集<small>特集一覧</small></h2>
      <p class="pick-head">注目特集ピックアップ</p>
      <div class="pick-grid">
        <div class="pick"><div class="pick-photo" role="img" aria-label="南国の海辺の写真"></div><p>海外旅行にお得な一枚を選ぶポイントを紹介</p></div>
        <div class="pick"><div class="pick-photo" role="img" aria-label="南国の海辺の写真"></div><p>旅行保険の付帯条件をわかりやすく解説</p></div>
        <div class="pick"><div class="pick-photo" role="img" aria-label="南国の海辺の写真"></div><p>マイルを効率よく貯める使い方のコツ</p></div>
        <div class="pick"><div class="pick-photo" role="img" aria-label="南国の海辺の写真"></div><p>空港ラウンジが使えるカードの比較</p></div>
        <div class="pick"><div class="pick-photo" role="img" aria-label="南国の海辺の写真"></div><p>海外での支払いと手数料の基本</p></div>
        <div class="pick"><div class="pick-photo" role="img" aria-label="南国の海辺の写真"></div><p>旅先で困らないカードの持ち方</p></div>
      </div>
      <div class="link-block">
        <h4>その他の特集</h4>
        <ul class="link-grid">
          <li>初めてのカード選び</li><li>ポイント活用術</li><li>年会費の考え方</li>
          <li>家計管理に役立つ</li><li>ネット通販の使い方</li><li>安全な使い方</li>
        </ul>
      </div>
      <p class="more"><a>特集一覧を見る</a></p>
    </section>

    <section class="section">
      <h2 class="section-title">スタイル別おすすめクレジットカード<small>スタイル別</small></h2>
      <div class="life">
        <div class="life-cards">
          <div class="life-card"><h3><span class="q">Q</span>はじめてならこれ！<br>初めてのクレジットカードなら？</h3><div class="card-visual" role="img" aria-label="カード券面"></div><p>年会費無料で審査にも配慮されたカードです。学生や新社会人の最初の一枚として選ばれています。</p></div>
          <div class="life-card"><h3><span class="q alt">Q</span>ジワジワと貯まる！<br>日常の買い物で一番お得なのは？</h3><div class="card-visual" role="img" aria-label="カード券面"></div><p>スーパーやコンビニでポイントが貯まりやすいカードです。毎日の支払いをまとめるだけでお得です。</p></div>
        </div>
        <p class="life-banner">ライフスタイルに合ったカードを探すには</p>
        <p class="life-text">当サイトの独自スタイル診断で、あなたにぴったりのクレジットカードが見つかります。<br><span class="hl">▶ ゴールドカード ▶ 年会費無料 ▶ ポイント重視 ▶ 旅行好き</span><br>いくつかの質問に答えるだけで、おすすめのカードを一覧で表示します。</p>
        <div class="life-buttons"><a class="btn">診断する</a><a class="btn blue">一覧から選ぶ</a></div>
      </div>
    </section>
  </main>

  <aside class="side">
    <div class="side-banner">ご利用金額に応じて<strong>最大3%</strong>キャッシュバック</div>
    <div class="side-box">
      <h2 class="section-title">今月のおすすめカード</h2>
      <div class="body"><div class="card-visual" role="img" aria-label="カード券面"></div><p>年会費無料でポイントが貯まる人気のカード。入会特典も充実しています。</p></div>
    </div>
    <div class="side-box">
      <h2 class="section-title">おすすめ入会キャンペーン</h2>
      <div class="campaign"><h5>ソラ銀カード</h5><div class="tag">期間限定キャンペーン</div><p class="note">新規入会で最大5,000円分プレゼント（〜2011年9月30日まで）</p></div>
      <div class="campaign"><h5>ミライポイントカード</h5><div class="tag">タイアップキャンペーン</div><p class="note">入会とご利用で最大8,000ポイント（〜2011年9月30日まで）</p></div>
      <div class="campaign"><h5>ナギサゴールドカード</h5><div class="tag">特別入会キャンペーン</div><p class="note">初年度年会費無料に加え特典付き（〜2011年9月30日まで）</p></div>
      <div class="campaign"><h5>ホシノカードプラス</h5><div class="tag">タイアップキャンペーン</div><p class="note">ネット入会で最大3,000円分還元（〜2011年9月30日まで）</p></div>
    </div>
  </aside>
</div>

<footer class="site-footer">
  <div>
    <div class="search"><span></span><b>検索</b></div>
    <p style="margin-top:12px">サイトマップ ｜ 運営者情報 ｜ プライバシーポリシー ｜ お問い合わせ</p>
  </div>
  <p>© カード選びナビ広場 All Rights Reserved.</p>
</footer>
</body>
</html>
```